Nicht nur, dass ich mit dem Design sehr zufrieden war, auch Änderungswünsche wurden zeitnah und zu meiner vollen Zufriedenheit ausgeführt.
Zielgruppe
Ich schreibe Kriminalromane
Zielgruppe sind die Leser von Kriminalromanen, Regionalkrimis
Aufgabenstellung
Hier handelt es sich um eine Kindesentführung im ländlichen Raum (Bayerischer Wald) ein Mosaik von Inzest und Tod.
Der Titel in moderner Schrift, angelehnt an die Titel der Skandinavienkrimis, sollte auch in kleiner Abbildung gut lesbar sein.
Es kommen in Kürze zwei weitere Titel, ebenfalls Kriminalromane, das Cover sollte also so gestaltet sein, dass eine durchgängige Reihe möglich ist.

```html
<!DOCTYPE html>
<html lang="de">
<head>
<meta charset="utf-8">
<title>Die Akte Wendel – Buchcover</title>
<link rel="stylesheet" href="https://fonts.googleapis.com/css2?family=Arimo:wght@400;700&display=swap">
<style>
  :root {
    --page-bg: #e6e6e6;
    --cover-black: #000000;
    --title-red: #d0181c;
    --title-white: #ffffff;
    --sky-pale: #ece6e2;
    --brick: #8a5a4c;
    --timber-dark: #3a2a26;
    --plum: #7a2a48;
  }
  * { box-sizing: border-box; margin: 0; padding: 0; }
  html, body {
    width: 1200px;
    height: 960px;
    overflow: hidden;
    background: var(--page-bg);
  }
  .cover {
    position: absolute;
    left: 259px;
    top: 30px;
    width: 682px;
    height: 900px;
    background: var(--cover-black);
  }
  .cover-photo {
    position: absolute;
    left: 143px;
    top: 152px;
    width: 394px;
    height: 559px;
    background: linear-gradient(180deg,
      var(--sky-pale) 0%,
      var(--sky-pale) 17%,
      var(--brick) 30%,
      #9a6d5c 50%,
      var(--timber-dark) 68%,
      var(--plum) 88%,
      #b04a78 100%);
  }
  .title {
    position: absolute;
    left: 142px;
    top: 560px;
    font-family: "Arimo", Arial, sans-serif;
    font-weight: 700;
    color: var(--title-white);
  }
  .title-line {
    display: table;
    background: var(--title-red);
    font-size: 66px;
    line-height: 72px;
    padding: 0 12px 0 10px;
    letter-spacing: -0.5px;
  }
  .title-line + .title-line { margin-top: 8px; }
  .byline {
    position: absolute;
    left: 142px;
    top: 721px;
    background: var(--title-red);
    color: var(--title-white);
    font-family: "Arimo", Arial, sans-serif;
    font-weight: 400;
    font-size: 12px;
    line-height: 20px;
    padding: 0 6px;
  }
</style>
</head>
<body>
  <div class="cover">
    <div class="cover-photo" role="img" aria-label="Blick durch ein regennasses Sprossenfenster auf Fachwerkhaus, Kirchtürme und bewachsene Mauer"></div>
    <h1 class="title">
      <span class="title-line">DIE AKTE</span>
      <span class="title-line">WENDEL</span>
    </h1>
    <p class="byline">Kriminalroman I Lukas Brandmeier</p>
  </div>
</body>
</html>
```